Fabric Softener

We need fabric softener. Bottle picture attached for reference. Color of bottle can be proposed as well. Normally bottle is pink and blue color

Logo is also attached that shall be used.
Updates

Need extra days to review

Low designer entries

Target Market(s)

Niche

Font styles to use
Sans Serif

Requirements
Must have
• Fabric, Brightness, Nature
Nice to have
• Good colors
Should not have
• Adults

```html
<!DOCTYPE html>
<html lang="en">
<head>
<meta charset="utf-8">
<title>Lumena Fabric Softener Labels</title>
<link href="https://fonts.googleapis.com/css2?family=Roboto+Condensed:wght@400;700&family=Ubuntu:ital,wght@0,400;1,500&display=swap" rel="stylesheet">
<style>
  :root{
    --bg-top:#6f4fab;
    --bg-bottom:#553791;
    --ink:#2b2b2b;
    --ink-soft:#3a3a3a;
    --lavender:#6a4fa9;
    --lily:#557d1c;
    --rose:#d9339f;
    --sky:#b9d7f0;
  }
  html,body{margin:0;padding:0;overflow:hidden}
  body{width:800px;height:1200px;background:linear-gradient(180deg,var(--bg-top),var(--bg-bottom));position:relative;font-family:"Roboto Condensed",sans-serif;color:var(--ink)}
  .label{position:absolute;width:523px;height:648px;transform-origin:0 0}
  .label--lavender{left:120px;top:21px;--accent:var(--lavender)}
  .label--lily{left:19px;top:691px;transform:scale(.704);--accent:var(--lily)}
  .label--rose{left:416px;top:691px;transform:scale(.704);--accent:var(--rose)}
  .label__shape{position:absolute;inset:0;width:523px;height:648px}
  .label > div,.label > p{position:absolute;margin:0}
  .flower-art{left:300px;top:22px;width:150px;height:106px;border-radius:50% 50% 40% 40%;opacity:.85}
  .label--lavender .flower-art{background:radial-gradient(ellipse at 50% 45%,#8f6fd0,#b9a2e6 55%,rgba(185,215,240,0) 75%)}
  .label--lily .flower-art{background:radial-gradient(ellipse at 45% 45%,#ffffff,#f7d58a 50%,rgba(185,215,240,0) 75%)}
  .label--rose .flower-art{background:radial-gradient(ellipse at 45% 45%,#e85aa3,#f3a6cc 50%,rgba(185,215,240,0) 75%)}
  .brand{left:300px;top:92px;width:160px;text-align:center;font-weight:700;font-size:34px;color:#5b45a0;display:flex;align-items:center;justify-content:center;gap:6px}
  .brand__dot{width:10px;height:10px;border-radius:50%;background:#5b45a0}
  .product-name{left:270px;top:156px;width:250px;text-align:center;font-family:"Ubuntu",sans-serif;font-style:italic;font-weight:500;font-size:26px;color:var(--accent);letter-spacing:-.3px}
  .scent{left:270px;top:186px;width:250px;text-align:center;font-family:"Ubuntu",sans-serif;font-size:12px;letter-spacing:.6px;color:var(--accent)}
  .section-title{font-weight:700;text-transform:uppercase;color:var(--accent);text-align:center;line-height:15px}
  .formula-title{left:259px;top:242px;width:240px;font-size:15.5px}
  .formula-text{left:254px;top:276px;width:250px;text-align:center;font-size:12.5px;line-height:17px;color:var(--ink-soft)}
  .usage-title{left:179px;top:378px;width:200px;font-size:16px}
  .usage-text{left:18px;top:397px;width:490px;text-align:center;font-size:12.5px;line-height:15px;color:var(--ink-soft)}
  .usage-text b{color:var(--accent)}
  .warning{left:40px;top:481px;width:450px;text-align:center;font-size:13px;line-height:17px}
  .warning b{letter-spacing:.5px}
  .origin{left:74px;top:594px;width:140px;text-align:center;font-size:13px}
  .contact{left:238px;top:525px;font-size:13px;line-height:17px}
</style>
</head>
<body>
<svg width="0" height="0" style="position:absolute">
  <defs>
    <linearGradient id="fill-lavender" x1="0" y1="0" x2="0" y2="1">
      <stop offset="0" stop-color="#b5d4ef"/><stop offset=".32" stop-color="#ffffff"/><stop offset=".75" stop-color="#f6f3fd"/><stop offset="1" stop-color="#d9cdf6"/>
    </linearGradient>
    <linearGradient id="fill-lily" x1="0" y1="0" x2="0" y2="1">
      <stop offset="0" stop-color="#b5d4ef"/><stop offset=".32" stop-color="#ffffff"/><stop offset=".75" stop-color="#f6f8ef"/><stop offset="1" stop-color="#dde7c3"/>
    </linearGradient>
    <linearGradient id="fill-rose" x1="0" y1="0" x2="0" y2="1">
      <stop offset="0" stop-color="#b5d4ef"/><stop offset=".32" stop-color="#ffffff"/><stop offset=".75" stop-color="#fbf3fb"/><stop offset="1" stop-color="#f2cfee"/>
    </linearGradient>
    <path id="label-outline" d="M392,0 C455,0 500,60 512,160 C525,270 523,420 520,520 C516,610 470,640 330,646 C200,652 60,640 22,600 C2,575 0,520 2,420 C3,380 15,364 40,366 C120,372 180,350 240,270 C300,180 310,40 345,15 C360,4 375,0 392,0 Z"/>
  </defs>
</svg>

<section class="label label--lavender">
  <svg class="label__shape" viewBox="0 0 523 648"><use href="#label-outline" fill="url(#fill-lavender)"/></svg>
  <div class="flower-art" role="img" aria-label="Lavender sprigs illustration"></div>
  <div class="brand"><span class="brand__dot"></span>Lumena</div>
  <div class="product-name">Fabric Softener</div>
  <div class="scent">LAVANDER FRESH</div>
  <div class="section-title formula-title">What's inside our<br>safe &amp; effective formula</div>
  <p class="formula-text">Lorem ipsum el dolor dehydrogenated (plant-based softener). dipropylene glycol (synthetic processing aid) calcium chloride sodium carbonate (mineral-based pH adJuster more).</p>
  <div class="section-title usage-title">How to use</div>
  <p class="usage-text"><b>1.</b> Check the care labels on your items to ensure they are machine-washable, if they're hand wash only. <b>2.</b> Add the softener to the clean rinsing bucket, swirl with your hand to mix, and rinse your clothing in the solution for soft, smooth results. <b>3.</b> Always wash your hands after handling fabric softener to reduce the risk of irritation. While rare, those with very sensitive skin may notice a mild reaction if undiluted fabric conditioner is allowed to sit on the skin for long periods.</p>
  <p class="warning"><b>WARNING:</b> Keep out of reach of children. If product gets into eyes,<br>flush thoroughly with water. If swallowed, drink plenty of water.</p>
  <div class="origin">MADE IN USA</div>
  <p class="contact">Manufactured for: <b>Lumena Co</b><br>123 Lake Street, Adresshere. 1234 USA<br><b>1-000-211-456789</b><br><b>www.yourwebsitehere.com</b><br>info@youremailhere.com</p>
</section>

<section class="label label--lily">
  <svg class="label__shape" viewBox="0 0 523 648"><use href="#label-outline" fill="url(#fill-lily)"/></svg>
  <div class="flower-art" role="img" aria-label="White and yellow lily flowers illustration"></div>
  <div class="brand"><span class="brand__dot"></span>Lumena</div>
  <div class="product-name">Fabric Softener</div>
  <div class="scent">LILY SCENT</div>
  <div class="section-title formula-title">What's inside our<br>safe &amp; effective formula</div>
  <p class="formula-text">Lorem ipsum el dolor dehydrogenated (plant-based softener). dipropylene glycol (synthetic processing aid) calcium chloride sodium carbonate (mineral-based pH adJuster more).</p>
  <div class="section-title usage-title">How to use</div>
  <p class="usage-text"><b>1.</b> Check the care labels on your items to ensure they are machine-washable, if they're hand wash only. <b>2.</b> Add the softener to the clean rinsing bucket, swirl with your hand to mix, and rinse your clothing in the solution for soft, smooth results. <b>3.</b> Always wash your hands after handling fabric softener to reduce the risk of irritation. While rare, those with very sensitive skin may notice a mild reaction if undiluted fabric conditioner is allowed to sit on the skin for long periods.</p>
  <p class="warning"><b>WARNING:</b> Keep out of reach of children. If product gets into eyes,<br>flush thoroughly with water. If swallowed, drink plenty of water.</p>
  <div class="origin">MADE IN USA</div>
  <p class="contact">Manufactured for: <b>Lumena Co</b><br>123 Lake Street, Adresshere. 1234 USA<br><b>1-000-211-456789</b><br><b>www.yourwebsitehere.com</b><br>info@youremailhere.com</p>
</section>

<section class="label label--rose">
  <svg class="label__shape" viewBox="0 0 523 648"><use href="#label-outline" fill="url(#fill-rose)"/></svg>
  <div class="flower-art" role="img" aria-label="Pink roses with leaves illustration"></div>
  <div class="brand"><span class="brand__dot"></span>Lumena</div>
  <div class="product-name">Fabric Softener</div>
  <div class="scent">ROSE</div>
  <div class="section-title formula-title">What's inside our<br>safe &amp; effective formula</div>
  <p class="formula-text">Lorem ipsum el dolor dehydrogenated (plant-based softener). dipropylene glycol (synthetic processing aid) calcium chloride sodium carbonate (mineral-based pH adJuster more).</p>
  <div class="section-title usage-title">How to use</div>
  <p class="usage-text"><b>1.</b> Check the care labels on your items to ensure they are machine-washable, if they're hand wash only. <b>2.</b> Add the softener to the clean rinsing bucket, swirl with your hand to mix, and rinse your clothing in the solution for soft, smooth results. <b>3.</b> Always wash your hands after handling fabric softener to reduce the risk of irritation. While rare, those with very sensitive skin may notice a mild reaction if undiluted fabric conditioner is allowed to sit on the skin for long periods.</p>
  <p class="warning"><b>WARNING:</b> Keep out of reach of children. If product gets into eyes,<br>flush thoroughly with water. If swallowed, drink plenty of water.</p>
  <div class="origin">MADE IN USA</div>
  <p class="contact">Manufactured for: <b>Lumena Co</b><br>123 Lake Street, Adresshere. 1234 USA<br><b>1-000-211-456789</b><br><b>www.yourwebsitehere.com</b><br>info@youremailhere.com</p>
</section>
</body>
</html>
```